Business Card for boutique psychology business

Business card for boutique psychology practice in Melbourne. I want them to be relatively simply with the logo and backing colour taking up the front side. Then, text on the back, with my name; professional title (Clinical Psychologist); website - torvinpsychology.com.au; email: hello@torvinpsychology.com.au; insta: @torvin.psychology.emdr
Back should also have the words: Connect. Integrate. Evolve
Fonts used for logo are: Mikea Demo and Gotham Medium. Use something for back text that will compliment these.
Brand colours uploaded below. I'd like to see options in both olive and blush.

```html
<!DOCTYPE html>
<html lang="en">
<head>
<meta charset="utf-8">
<title>Torvin Psychology – Business Card</title>
<link rel="stylesheet" href="https://fonts.googleapis.com/css2?family=Josefin+Sans:wght@300;400&display=swap">
<style>
  :root {
    --backdrop: #2a2c2e;
    --olive: #4a4b2f;
    --blush: #f2cdb5;
    --card-w: 600px;
    --card-h: 343px;
  }
  * { margin: 0; padding: 0; box-sizing: border-box; }
  html, body { width: 1200px; height: 939px; overflow: hidden; }
  body { background: var(--backdrop); position: relative; font-family: 'Josefin Sans', sans-serif; color: var(--blush); }

  .card {
    position: absolute;
    width: var(--card-w);
    height: var(--card-h);
    background: var(--olive);
    box-shadow: 0 10px 30px rgba(0,0,0,.45);
  }
  .card--front { left: 90px; top: 80px; }
  .card--back  { left: 510px; top: 500px; }

  .brand-name {
    position: absolute;
    font-family: 'Josefin Sans', sans-serif;
    font-weight: 400;
    line-height: 1;
    color: var(--blush);
    white-space: nowrap;
  }
  .card--front .brand-name { left: 50%; top: 50%; transform: translate(-50%, -50%); font-size: 52px; }
  .card--back .brand-name { left: 160px; top: 142px; transform: translateX(-50%); font-size: 44px; }

  .divider { position: absolute; left: 318px; top: 92px; width: 1px; height: 130px; background: var(--blush); }

  .contact { position: absolute; left: 340px; top: 84px; }
  .contact__name { font-size: 22px; font-weight: 400; letter-spacing: 1.5px; }
  .contact__title { font-size: 12px; font-weight: 400; margin-top: 3px; padding-bottom: 6px; border-bottom: 1px solid var(--blush); width: 180px; }
  .contact__list { list-style: none; margin-top: 8px; font-size: 12.5px; line-height: 20px; }
  .contact__list li { display: flex; align-items: center; gap: 7px; }
  .contact__list svg { width: 11px; height: 11px; flex: none; }

  .tagline { position: absolute; left: 0; right: 0; bottom: 52px; text-align: center; font-size: 26px; font-weight: 300; letter-spacing: 1px; word-spacing: 6px; padding-left: 90px; }
</style>
</head>
<body>

<section class="card card--front" aria-label="Card front">
  <p class="brand-name">torvin</p>
</section>

<section class="card card--back" aria-label="Card back">
  <p class="brand-name">torvin</p>

  <div class="divider"></div>

  <div class="contact">
    <p class="contact__name">Dr. Mara Torvin</p>
    <p class="contact__title">Clinical Psychologist</p>
    <ul class="contact__list">
      <li>
        <svg viewBox="0 0 12 12" fill="var(--blush)"><path d="M2.5 1h2l1 2.8-1.3 1a6 6 0 0 0 2.9 2.9l1-1.3 2.9 1v2A1.3 1.3 0 0 1 9.6 11 8.8 8.8 0 0 1 1 2.4 1.3 1.3 0 0 1 2.5 1z"/></svg>
        0400 555 018
      </li>
      <li>
        <svg viewBox="0 0 12 12" fill="var(--blush)"><path d="M1 2.5h10v7H1z M1 2.5l5 4 5-4" stroke="var(--olive)" stroke-width=".8"/></svg>
        hello@torvinpsychology.com.au
      </li>
      <li>
        <svg viewBox="0 0 12 12" fill="none" stroke="var(--blush)" stroke-width="1"><circle cx="6" cy="6" r="5"/><ellipse cx="6" cy="6" rx="2.2" ry="5"/><path d="M1 6h10M2 3.5h8M2 8.5h8"/></svg>
        torvinpsychology.com.au
      </li>
      <li>
        <svg viewBox="0 0 12 12" fill="none" stroke="var(--blush)" stroke-width="1.2"><circle cx="6" cy="6" r="4.8"/></svg>
        @torvin.psychology.emdr
      </li>
    </ul>
  </div>

  <p class="tagline">Connect. Integrate. Evolve</p>
</section>

</body>
</html>
```